Harlow Solutions Website

My business has been word of mouth over the last 3 years and has grown. Now I need a website for additional marketing as we have new clients asking for a website.

You have already completed my Logo during an earlier project. I have attached the logo.

We do Staff Augmentation and Operation Support.

What is that?
Staff augmentation is an outsourcing strategy that allows companies to fill specific, temporary roles to achieve business objectives. This staffing method complements existing teams with specific talent, enhancing business capabilities or filling gaps left by members on extended leave.

We work alongside the internal recruiting team to assist clients to meet and exceed financial goals.

```html
<!DOCTYPE html>
<html lang="en">
<head>
<meta charset="UTF-8">
<title>Harlow Solutions</title>
<link href="https://fonts.googleapis.com/css2?family=Poppins:wght@400;500;600;700&family=Lato:wght@400;700&display=swap" rel="stylesheet">
<style>
:root{
  --navy:#0f4275;
  --navy-deep:#0c355f;
  --ink:#1f2530;
  --text:#4a4f57;
  --muted:#8a9099;
  --line:#d6dbe2;
  --paper:#ffffff;
  --mist:#eef0f3;
}
*{box-sizing:border-box;margin:0;padding:0}
html,body{width:1200px;height:3320px;overflow:hidden}
body{position:relative;background:var(--paper);font-family:'Lato',sans-serif;color:var(--text)}
.abs{position:absolute}
.heading{font-family:'Poppins',sans-serif}

/* header */
.brand{left:112px;top:18px;display:flex;align-items:center;gap:12px}
.brand-dot{width:50px;height:50px;border-radius:50%;background:var(--navy)}
.brand-name{font-family:'Poppins',sans-serif;font-weight:600;color:var(--navy);font-size:23px;line-height:1.05;letter-spacing:.5px}
.brand-name small{display:block;font-size:15px;font-weight:600}
.nav{top:32px;font-size:15px;color:var(--ink);font-family:'Lato',sans-serif}
.nav.active{color:var(--navy);border-bottom:2px solid var(--navy);padding-bottom:2px}
.social-mini{top:35px;width:14px;height:14px;border-radius:50%;background:var(--navy)}
.login{left:980px;top:22px;width:108px;height:42px;border-radius:21px;background:var(--navy);color:#fff;font-family:'Poppins',sans-serif;font-weight:600;font-size:14px;display:flex;align-items:center;justify-content:center}

/* hero */
.hero-bg{left:0;top:82px;width:600px;height:540px;background:linear-gradient(120deg,#f3f4f6 0%,#fbfbfc 55%,#ffffff 100%)}
.hero-panel{left:565px;top:82px;width:635px;height:538px;background:var(--mist)}
.hero-photo{left:589px;top:82px;width:611px;height:514px;background:linear-gradient(135deg,#c9b9a5 0%,#6f7d8e 45%,#2b3d57 100%)}
.welcome{left:111px;top:206px;font-size:44px;font-weight:400;color:var(--ink)}
.hero-title{left:109px;top:262px;font-size:51px;font-weight:700;color:var(--navy);white-space:nowrap}
.hero-copy{left:111px;top:336px;width:450px;font-size:15.5px;line-height:26px;color:var(--text)}
.btn-solid{background:var(--navy);color:#fff;border-radius:22px;font-family:'Poppins',sans-serif;font-weight:600;font-size:14px;display:flex;align-items:center;justify-content:center}
.hero-cta{left:113px;top:416px;width:150px;height:44px}
.play{left:292px;top:416px;width:44px;height:44px;border:1px solid var(--line);border-radius:50%;display:flex;align-items:center;justify-content:center}
.watch{left:345px;top:428px;font-family:'Poppins',sans-serif;font-weight:600;font-size:14px;color:var(--navy)}

/* section title */
.sec-title{width:1200px;left:0;text-align:center;font-family:'Poppins',sans-serif;font-weight:600;font-size:29px;color:var(--ink)}
.sec-title span{color:var(--navy)}

/* service cards */
.svc{top:782px;width:309px;height:463px;background:#fff;box-shadow:0 2px 10px rgba(0,0,0,.12);text-align:center}
.svc.featured{background:var(--navy);color:#fff}
.svc-photo{width:309px;height:207px}
.svc-icon{position:absolute;left:115px;top:168px;width:78px;height:78px;border-radius:50%;background:#fff;box-shadow:0 2px 8px rgba(0,0,0,.15);display:flex;align-items:center;justify-content:center}
.svc h3{position:absolute;top:278px;width:100%;font-family:'Poppins',sans-serif;font-weight:500;font-size:19px;color:var(--ink)}
.svc.featured h3{color:#fff}
.svc p{position:absolute;top:320px;left:34px;right:34px;font-size:15px;line-height:26px;text-align:justify;text-align-last:center;color:var(--text)}
.svc.featured p{color:#dfe7f1}
.svc .more{position:absolute;top:415px;width:100%;font-family:'Poppins',sans-serif;font-weight:600;font-size:14px;color:var(--navy)}
.svc.featured .more{color:#fff}

/* about */
.about-band{left:0;top:1344px;width:1200px;height:515px;background:linear-gradient(90deg,var(--navy-deep),var(--navy) 60%,#124a82);border-radius:190px 0 190px 0;overflow:hidden}
.about-ring{left:100px;top:1420px;width:390px;height:390px;border-radius:50%;border:34px solid rgba(255,255,255,.08)}
.about-photo{left:159px;top:1487px;width:270px;height:270px;border-radius:50%;background:linear-gradient(135deg,#b99a7a,#5b6c80 60%,#2d3e54);border:4px solid rgba(255,255,255,.85)}
.about-title{left:598px;top:1418px;font-family:'Poppins',sans-serif;font-weight:600;font-size:29px;color:#fff}
.about-copy{left:598px;top:1476px;width:485px;font-size:16px;line-height:25.8px;color:#e4ebf4;text-align:justify}
.btn-light{left:606px;top:1732px;width:146px;height:44px;background:#fff;color:var(--navy);border-radius:22px;font-family:'Poppins',sans-serif;font-weight:600;font-size:14px;display:flex;align-items:center;justify-content:center}

/* team */
.member{top:2033px;width:230px;height:298px;background:#fff;border-radius:50px 0 50px 0;box-shadow:0 2px 10px rgba(0,0,0,.12);text-align:center}
.member-photo{position:absolute;left:50px;top:22px;width:130px;height:130px;border-radius:50%;background:linear-gradient(160deg,#c8cfd8,#55606e)}
.member.featured .member-photo{border:5px solid var(--navy);left:44px;top:16px;width:142px;height:142px}
.member h4{position:absolute;top:172px;width:100%;font-family:'Poppins',sans-serif;font-weight:500;font-size:18px;color:var(--ink)}
.member .role{position:absolute;top:201px;width:100%;font-size:15px;color:var(--navy)}
.member .links{position:absolute;top:237px;left:0;width:100%;display:flex;justify-content:center;gap:15px}
.member .links span{width:38px;height:38px;border-radius:50%;border:1px solid var(--navy)}
.member.featured .links span{background:var(--navy)}

/* contact */
.contact-band{left:0;top:2434px;width:1200px;height:515px;background:linear-gradient(90deg,var(--navy-deep),var(--navy));border-radius:190px 0 190px 0}
.contact-card{left:268px;top:2497px;width:665px;height:389px;background:#fff}
.contact-title{left:268px;width:665px;top:2533px;text-align:center;font-family:'Poppins',sans-serif;font-weight:600;font-size:29px;color:var(--navy)}
.field{height:48px;width:294px;border:1px solid var(--line);border-radius:3px;font-size:14px;color:var(--muted);padding:0 20px;display:flex;align-items:center;justify-content:space-between}
.field.msg{width:602px;height:83px;align-items:flex-start;padding-top:16px}
.submit{left:528px;top:2820px;width:142px;height:42px}

/* footer */
.foot-brand{left:112px;top:3046px;display:flex;align-items:center;gap:14px}
.foot-brand .brand-dot{width:62px;height:62px}
.foot-brand .brand-name{font-size:36px}
.foot-brand .brand-name small{font-size:23px}
.tagline{left:112px;top:3150px;width:282px;font-size:15px;line-height:26px;color:var(--ink);text-align:justify}
.foot-h{top:3032px;font-family:'Poppins',sans-serif;font-weight:500;font-size:18px;color:var(--ink)}
.foot-links{left:476px;top:3064px;font-size:15px;line-height:26px;color:var(--text);list-style:none}
.foot-item{left:664px;display:flex;gap:12px;font-size:15px;line-height:22px;color:var(--ink)}
.follow{top:3069px;width:38px;height:38px;border-radius:50%;background:var(--navy)}
.rule{left:112px;top:3238px;width:976px;height:1px;background:var(--line)}
.copy{left:0;width:1200px;top:3268px;text-align:center;font-size:15px;color:var(--ink)}
</style>
</head>
<body>

<!-- header -->
<div class="abs brand"><span class="brand-dot"></span><div class="brand-name">HARLOW<small>SOLUTIONS,LLC</small></div></div>
<div class="abs nav active" style="left:453px">Home</div>
<div class="abs nav" style="left:533px">About</div>
<div class="abs nav" style="left:612px">Services</div>
<div class="abs nav" style="left:708px">Team</div>
<div class="abs nav" style="left:785px">Contact</div>
<span class="abs social-mini" style="left:865px" aria-label="Social profile"></span>
<span class="abs social-mini" style="left:896px" aria-label="Social profile"></span>
<span class="abs social-mini" style="left:932px" aria-label="Social profile"></span>
<div class="abs login">LOG IN</div>

<!-- hero -->
<div class="abs hero-bg"></div>
<div class="abs hero-panel"></div>
<div class="abs hero-photo" role="img" aria-label="Photo of two business colleagues reviewing a tablet in a modern office"></div>
<h2 class="abs welcome heading">Welcome</h2>
<h1 class="abs hero-title heading">Harlow Solutions</h1>
<p class="abs hero-copy">Lorem ipsum dolor sit amet, consectetur adipiscing elit, sed do eiusmod tempor incididunt ut labore et dolore magna aliqua.</p>
<div class="abs btn-solid hero-cta">GET SOLUTION</div>
<div class="abs play"><svg width="10" height="12" viewBox="0 0 10 12"><path d="M1 1l8 5-8 5z" fill="var(--navy)"/></svg></div>
<div class="abs watch">WATCH VIDEO</div>

<!-- services -->
<h2 class="abs sec-title" style="top:698px"><span>OUR</span> SERVICES</h2>

<div class="abs svc" style="left:112px">
  <div class="svc-photo" role="img" aria-label="Photo of a support agent with a headset at his desk" style="background:linear-gradient(135deg,#d9dde2,#8a96a4 60%,#4b5563)"></div>
  <div class="svc-icon"><svg width="36" height="36" viewBox="0 0 36 36" fill="none" stroke="var(--navy)" stroke-width="1.6"><circle cx="18" cy="13" r="6"/><path d="M9 14a9 9 0 0118 0M8 30c1-6 5-9 10-9s9 3 10 9z"/></svg></div>
  <h3>Operation Support</h3>
  <p>Lorem ipsum dolor sit amet, consectetur adipiscing elit, sed doeiusmod tempor</p>
  <div class="more">LEARN MORE &#8250;</div>
</div>

<div class="abs svc featured" style="left:445px">
  <div class="svc-photo" role="img" aria-label="Photo of a team of colleagues meeting in a bright office" style="background:linear-gradient(135deg,#e2e2de,#9ba3ad 55%,#545e6b)"></div>
  <div class="svc-icon"><svg width="40" height="36" viewBox="0 0 40 36" fill="none" stroke="var(--navy)" stroke-width="1.6"><circle cx="10" cy="10" r="5"/><circle cx="28" cy="16" r="5"/><path d="M3 28c1-5 4-8 7-8M20 34c1-6 4-9 8-9s7 3 8 9z"/></svg></div>
  <h3>Staff Augmentation</h3>
  <p>Lorem ipsum dolor sit amet, consectetur adipiscing elit, sed doeiusmod tempor</p>
  <div class="more">LEARN MORE &#8250;</div>
</div>

<div class="abs svc" style="left:779px">
  <div class="svc-photo" role="img" aria-label="Photo of a professional checking records on a phone beside a computer" style="background:linear-gradient(135deg,#f0eeea,#b7b1a6 50%,#3a3630)"></div>
  <div class="svc-icon"><svg width="36" height="36" viewBox="0 0 36 36" fill="none" stroke="var(--navy)" stroke-width="1.6"><path d="M8 4h16v26H8z"/><path d="M12 10h8M12 15h8M12 20h4"/><circle cx="24" cy="24" r="5"/><path d="M28 28l4 4"/></svg></div>
  <h3>Background verification</h3>
  <p>Lorem ipsum dolor sit amet, consectetur adipiscing elit, sed doeiusmod tempor</p>
  <div class="more">LEARN MORE &#8250;</div>
</div>

<!-- about -->
<div class="abs about-band" role="img" aria-label="Navy band with a faint city skyline"></div>
<div class="abs about-ring"></div>
<div class="abs about-photo" role="img" aria-label="Photo of two colleagues working together at a laptop"></div>
<h2 class="abs about-title">ABOUT HARLOW SOLUTIONS</h2>
<p class="abs about-copy">Lorem ipsum dolor sit amet, consectetur adipiscing elit, sed do eiusmod tempor incididunt ut labore et dolore magna aliqua. Ut enim ad minim veniam, quis nostrud exercitation ullamco laboris nisi ut aliquip ex ea commodo consequat. Duis aute irure dolor in reprehenderit in voluptate velit esse cillum dolore eu fugiat nulla pariatur. Excepteur sint occaecat cupidatat non proident, sunt in culpa qui officia deserunt mollit anim id est laborum.Sed ut perspiciatis unde omnis iste natus error sit voluptatem accusantium doloremque laudantium, totam rem aperiam.</p>
<div class="abs btn-light">GET SOLUTION</div>

<!-- team -->
<h2 class="abs sec-title" style="top:1939px"><span>OUR</span> TEAM</h2>

<div class="abs member" style="left:112px">
  <div class="member-photo" role="img" aria-label="Portrait photo of a team member"></div>
  <h4>MERRIDEW</h4><div class="role">Lorem ipsum</div>
  <div class="links"><span></span><span></span><span></span></div>
</div>
<div class="abs member featured" style="left:360px">
  <div class="member-photo" role="img" aria-label="Portrait photo of a team member" style="background:linear-gradient(160deg,#8a2b3a,#3a1d24)"></div>
  <h4>MERRIDEW</h4><div class="role">Lorem ipsum</div>
  <div class="links"><span></span><span></span><span></span></div>
</div>
<div class="abs member" style="left:610px">
  <div class="member-photo" role="img" aria-label="Portrait photo of a team member"></div>
  <h4>MERRIDEW</h4><div class="role">Lorem ipsum</div>
  <div class="links"><span></span><span></span><span></span></div>
</div>
<div class="abs member" style="left:857px">
  <div class="member-photo" role="img" aria-label="Portrait photo of a team member" style="background:linear-gradient(160deg,#a9c0d8,#1f3a66)"></div>
  <h4>MERRIDEW</h4><div class="role">Lorem ipsum</div>
  <div class="links"><span></span><span></span><span></span></div>
</div>

<!-- contact -->
<div class="abs contact-band"></div>
<div class="abs contact-card"></div>
<h2 class="abs contact-title">CONTACT US</h2>
<div class="abs field" style="left:299px;top:2597px">Full Name<svg width="12" height="12" viewBox="0 0 12 12" fill="#9aa0a8"><circle cx="6" cy="3.5" r="3"/><path d="M0 12c0-4 3-5 6-5s6 1 6 5z"/></svg></div>
<div class="abs field" style="left:607px;top:2597px">Company Name<svg width="12" height="12" viewBox="0 0 12 12" fill="#9aa0a8"><path d="M6 0l6 5v7H8V8H4v4H0V5z"/></svg></div>
<div class="abs field" style="left:299px;top:2658px">Email ID<svg width="14" height="11" viewBox="0 0 14 11" fill="#9aa0a8"><path d="M0 0h14v11H0z"/><path d="M0 0l7 6 7-6" stroke="#fff" fill="none"/></svg></div>
<div class="abs field" style="left:607px;top:2658px">Phone Number<svg width="12" height="12" viewBox="0 0 12 12" fill="#9aa0a8"><path d="M2 0l3 3-1.5 2a7 7 0 003.5 3.5L9 7l3 3-2 2C5 12 0 7 0 2z"/></svg></div>
<div class="abs field msg" style="left:299px;top:2717px">Message</div>
<div class="abs btn-solid submit">SUBMIT NOW</div>

<!-- footer -->
<div class="abs foot-brand"><span class="brand-dot"></span><div class="brand-name">HARLOW<small>SOLUTIONS,LLC</small></div></div>
<p class="abs tagline">We do Staff Augmentation and Operation Support Lorem ipsum dolor sit</p>

<h3 class="abs foot-h" style="left:476px">QUICK LINKS</h3>
<ul class="abs foot-links"><li>Home</li><li>About</li><li>Services</li><li>Team</li><li>Contact</li></ul>

<h3 class="abs foot-h" style="left:664px">CONTACT US</h3>
<div class="abs foot-item" style="top:3066px"><svg width="14" height="18" viewBox="0 0 14 18"><path d="M7 0a7 7 0 017 7c0 5-7 11-7 11S0 12 0 7a7 7 0 017-7z" fill="var(--ink)"/><circle cx="7" cy="7" r="2.5" fill="#fff"/></svg><span>Lorem ipsum dolor sit<br>amet, consectetur</span></div>
<div class="abs foot-item" style="top:3126px"><svg width="14" height="14" viewBox="0 0 12 12" fill="var(--ink)"><path d="M2 0l3 3-1.5 2a7 7 0 003.5 3.5L9 7l3 3-2 2C5 12 0 7 0 2z"/></svg><span>+1 (555) 014 2290</span></div>
<div class="abs foot-item" style="top:3163px"><svg width="16" height="12" viewBox="0 0 14 11"><path d="M0 0h14v11H0z" fill="var(--ink)"/><path d="M0 0l7 6 7-6" stroke="#fff" fill="none"/></svg><span>info@harlowsolutions.com</span></div>

<h3 class="abs foot-h" style="left:911px">FOLLOW US</h3>
<span class="abs follow" style="left:912px" aria-label="Social profile"></span>
<span class="abs follow" style="left:958px" aria-label="Social profile"></span>
<span class="abs follow" style="left:1003px" aria-label="Social profile"></span>
<span class="abs follow" style="left:1049px" aria-label="Social profile"></span>

<div class="abs rule"></div>
<p class="abs copy">©Copyrights 2022 Harlow Solutions &nbsp;| &nbsp;All Rights Reserved</p>

</body>
</html>
```